Menu revision for Korean Restaurant

I have posted the exact content in a word file that I would like to appear in the menu. Please apply to the template. I will be following up with prices shortly. I am in a hurry and not too picky. Thank you.

Make a menu with revisions.

Page 1: Cover Page
- Replace logo with new uploaded logo

Page 2:
Appetizers
Vegetarian Appetizers

Page 3:
BBQ Items

Page 4:
Signature Dishes

Page 5:
Bokkeum | Stir-Fry

Page 6:
Rice Bowls
Noodles
Hot Soup

Page 7:
Drinks

Target Market(s)

My customers

Industry/Entity Type

Restaurant

Requirements
Must have
• 1. Only use my menu content, template, and font.

```html
<!DOCTYPE html>
<html lang="en">
<head>
<meta charset="utf-8">
<title>Bokkeum | Stir-Fry</title>
<link rel="stylesheet" href="https://fonts.googleapis.com/css2?family=Saira:wght@700;800&family=Lora:wght@400;600&family=Nanum+Gothic:wght@400;700&display=swap">
<style>
  :root {
    --bg: #121415;
    --gold: #b49a52;
    --gold-line: #8f7a44;
    --red: #b3151d;
    --text: #e9e6df;
    --veg: #2fc42a;
    --photo-top: #2a1a12;
    --photo-mid: #b8431c;
    --photo-low: #d9d4c8;
  }
  * { margin: 0; padding: 0; box-sizing: border-box; }
  html, body { width: 927px; height: 1200px; overflow: hidden; background: var(--bg); }
  .page { position: relative; width: 927px; height: 1200px; background: var(--bg); color: var(--text); font-family: "Lora", serif; }
  .frame { position: absolute; inset: 0; }
  .title {
    position: absolute; top: 50px; left: 0; width: 927px; text-align: center;
    font-family: "Saira", sans-serif; font-weight: 800; font-size: 50px; line-height: 60px;
    letter-spacing: 9px; color: var(--red);
  }
  .title .sep { display: inline-block; width: 2px; height: 50px; background: var(--red); vertical-align: -6px; margin: 0 30px 0 22px; }
  .item {
    position: absolute; width: 388px; font-size: 15px; line-height: 21.6px;
    text-align: justify; letter-spacing: 0.6px;
  }
  .item .name { font-family: "Saira", sans-serif; font-weight: 700; color: var(--gold); letter-spacing: 1.2px; margin-right: 6px; }
  .item .ko { font-family: "Nanum Gothic", sans-serif; color: var(--gold); margin-right: 6px; letter-spacing: 1px; }
  .item .price { font-weight: 600; }
  .left { left: 54px; }
  .right { left: 482px; }
  .photo {
    position: absolute; width: 388px; height: 228px; border: 1px solid var(--gold-line);
    background: radial-gradient(ellipse 70% 45% at 50% 55%, var(--photo-mid), #7a2812 55%, transparent 75%),
                linear-gradient(180deg, var(--photo-top) 0%, #3a2418 55%, var(--photo-low) 70%, #1a120c 88%);
  }
  .photo .caption {
    position: absolute; top: 9px; left: 10px; font-family: "Saira", sans-serif; font-weight: 700;
    font-size: 11px; letter-spacing: 0.8px; color: #fff;
  }
  .photo .caption .ko { font-family: "Nanum Gothic", sans-serif; font-weight: 400; margin-left: 4px; }
  .rule { position: absolute; width: 388px; height: 46px; }
  .rule .line { position: absolute; top: 23px; width: 158px; height: 1px; background: var(--gold-line); }
  .rule .line.a { left: 0; }
  .rule .line.b { right: 0; }
  .rule .seal {
    position: absolute; left: 171px; top: 0; width: 46px; height: 46px; border-radius: 50%;
    border: 1.5px solid var(--gold-line); background: radial-gradient(circle, #6b5a32, #2a251a 70%);
  }
  .veg {
    display: inline-block; width: 16px; height: 16px; border-radius: 50%; background: var(--veg);
    color: #fff; font-family: "Lora", serif; font-style: italic; font-weight: 600; font-size: 13px;
    line-height: 16px; text-align: center;
  }
  .veg-mark { position: absolute; left: 424px; top: 624px; }
  .footer { position: absolute; top: 1149px; left: 78px; font-size: 12px; letter-spacing: 0.5px; }
  .footer .veg { margin: 0 6px 0 18px; vertical-align: -3px; }
</style>
</head>
<body>
<div class="page">
  <svg class="frame" width="927" height="1200" viewBox="0 0 927 1200" aria-hidden="true">
    <g fill="none" stroke="#8f7a44" stroke-width="1.5">
      <path d="M66 16 H860 V64 H906 V1134 H860 V1182 H66 V1134 H20 V64 H66 Z"/>
      <rect x="38" y="35" width="19" height="19"/>
      <rect x="869" y="35" width="19" height="19"/>
      <rect x="38" y="1144" width="19" height="19"/>
      <rect x="869" y="1144" width="19" height="19"/>
    </g>
  </svg>

  <h1 class="title">BOKKEUM<span class="sep"></span>STIR-FRY</h1>

  <p class="item left" style="top:144px"><span class="name">JEYUK BOKKEUM</span><span class="ko">제육볶음</span>Pork, onions, scallions, mushrooms and jalapenos stir-fried in a spicy red garlic sauce. <span class="price">$15.95</span></p>

  <div class="photo" style="left:54px;top:234px" role="img" aria-label="Plate of glazed pork in red chili sauce"><span class="caption">DWAEJI BOSSAM<span class="ko">돼지보쌈</span></span></div>

  <div class="rule" style="left:54px;top:484px"><span class="line a"></span><span class="seal" role="img" aria-label="Round seal emblem"></span><span class="line b"></span></div>

  <p class="item left" style="top:547px"><span class="name">DUBU BOKKEUM</span><span class="ko">두부볶음</span>Fried tofu cubes, zucchini, carrots, onions, and mushrooms stir-fried in a red chili sauce. <span class="price">$13.95</span></p>
  <span class="veg veg-mark">v</span>

  <div class="rule" style="left:54px;top:631px"><span class="line a"></span><span class="seal" role="img" aria-label="Round seal emblem"></span><span class="line b"></span></div>

  <p class="item left" style="top:694px"><span class="name">KIMCHI BOKKEUM</span><span class="ko">김치볶음</span>Pork, kimchi, rice cakes, scallions, onions, and fresh tofu. <span class="price">$15.95</span></p>

  <div class="photo" style="left:54px;top:762px" role="img" aria-label="Plate of glazed dumplings in red chili sauce"><span class="caption">SAMPLE TEXT<span class="ko">군만두</span></span></div>

  <p class="item right" style="top:140px"><span class="name">HAEMUL BOKKEUM</span><span class="ko">해물볶음</span>Jumbo shrimp, scallops, mussels, calamari, octopus, zucchini, carrots, onions, scallions, mushrooms, and jalapenos <span class="price">$17.95</span></p>

  <div class="rule" style="left:482px;top:235px"><span class="line a"></span><span class="seal" role="img" aria-label="Round seal emblem"></span><span class="line b"></span></div>

  <p class="item right" style="top:300px"><span class="name">SAMGYUPSAL BOKKEUM</span><span class="ko">매운삼겹살</span>Pork belly, zucchini, onions, scallions stir-fried in a spicy gochu wine sauce. <span class="price">$15.95</span></p>

  <div class="rule" style="left:482px;top:389px"><span class="line a"></span><span class="seal" role="img" aria-label="Round seal emblem"></span><span class="line b"></span></div>

  <p class="item right" style="top:453px"><span class="name">OJINGEO BOKKEUM</span><span class="ko">오징어볶음</span>Fresh calamari stir-fried with carrots, zucchini, mushrooms, onions and scallions in a hot and spicy chili sauce. <span class="price">$15.95</span></p>

  <div class="photo" style="left:482px;top:558px" role="img" aria-label="Plate of spicy stir-fried calamari in red chili sauce"><span class="caption">OJINGEO BOKKEUM<span class="ko">오징어볶음</span></span></div>

  <div class="rule" style="left:482px;top:809px"><span class="line a"></span><span class="seal" role="img" aria-label="Round seal emblem"></span><span class="line b"></span></div>

  <p class="item right" style="top:874px"><span class="name">NAKJI BOKKEUM</span><span class="ko">낙지볶음</span>Fresh octopus stir-fried with carrots, zucchini, mushrooms, onions, and scallions in a hot and spicy chili sauce. <span class="price">$15.95</span></p>

  <div class="rule" style="left:482px;top:963px"><span class="line a"></span><span class="seal" role="img" aria-label="Round seal emblem"></span><span class="line b"></span></div>

  <p class="item right" style="top:1030px"><span class="name">JJUGGUMI SAMGYUPSAL</span><span class="ko">쭈꾸미삼겹살</span>Spicy pork belly and baby octopus. <span class="price">$18.95</span></p>

  <p class="footer">*Jeon batter contains wheat flour &amp; eggs.<span class="veg">v</span>Vegetarian</p>
</div>
</body>
</html>
```